We need a laundry sheet packingbox desgin

-look at our website kribbelnest.nl to be in line with our house style/collor
We are a perfume seller and would like to offer also wasshingsheets with NO SMELL, so the customers can buy this incombination with our washingperfumes.
-the wassingheets will be neutrale(NO SMELL)
-it will be for the Dutch market
The next points should be on the desgin of the package
-our brand name: KRIBBELNEST
-product name: WASSTRIPS
-(contains) Bevat: 30 wasstrips
-30 wasstrips = 60 wasbeurten
Please take some inspiration of others sellers & regarding eco friendly symbols etc.:
velondra.com & plumtak.nl
Backside information will be provided afther we found the right desgin
Please look at attachement pdf open box.
Here you can find the pdf design where you need to customize:
https://qx.vz/t-rKbWnHs4Lp

```html
<!DOCTYPE html>
<html lang="nl">
<head>
<meta charset="UTF-8">
<title>Kribbelnest Wasstrips – verpakking voorzijde</title>
<link rel="stylesheet" href="https://fonts.googleapis.com/css2?family=Cinzel:wght@400&family=Montserrat:wght@400;500;600&display=swap">
<style>
  :root {
    --page-bg: #dedede;
    --box-black: #1c1c1c;
    --box-black-deep: #141414;
    --gold: #c9a24a;
    --gold-deep: #a4782a;
    --gold-side: #966f26;
    --gold-side-light: #a57b2c;
    --ink-dark: #1a1408;
    --white: #f2f2f2;
    --line-grey: #3a3a3a;
  }
  * { box-sizing: border-box; margin: 0; padding: 0; }
  html, body { width: 1200px; height: 800px; overflow: hidden; background: var(--page-bg); }
  .canvas { position: relative; width: 1200px; height: 800px; }

  .box-front {
    position: absolute; left: 357px; top: 40px; width: 435px; height: 720px;
    background: linear-gradient(90deg, var(--box-black) 60%, var(--box-black-deep));
    overflow: hidden;
  }
  .box-side {
    position: absolute; left: 792px; top: 40px; width: 50px; height: 720px;
    background: linear-gradient(90deg, var(--gold-side), var(--gold-side-light) 60%, var(--gold-side));
    display: flex; align-items: center; justify-content: center;
  }
  .box-side__brand {
    writing-mode: vertical-rl;
    font-family: "Cinzel", serif; font-size: 9px; letter-spacing: 1.5px;
    color: var(--ink-dark);
  }

  .box-front__content {
    position: absolute; left: 0; top: 0; width: 720px; height: 435px;
    transform-origin: 0 0;
    transform: translateY(720px) rotate(-90deg);
    font-family: "Montserrat", sans-serif;
  }
  .halftone-area {
    position: absolute; left: 450px; top: 200px; width: 270px; height: 235px;
    background: radial-gradient(ellipse at 100% 100%, #2e2e2e 0%, #242424 45%, rgba(28,28,28,0) 80%);
  }
  .window-outline { position: absolute; inset: 0; }

  .brand-name {
    position: absolute; left: 318px; top: 153px;
    font-family: "Cinzel", serif; font-size: 13px; letter-spacing: 1px; line-height: 1;
    color: var(--gold);
  }
  .product-title {
    position: absolute; left: 130px; top: 165px; height: 80px;
    display: flex; align-items: center; gap: 8px;
  }
  .product-name {
    font-size: 52px; font-weight: 500; letter-spacing: 6px; line-height: 1;
    color: var(--white);
  }
  .product-badge { width: 80px; height: 80px; flex: none; }

  .washer-illustration {
    position: absolute; left: 434px; top: 292px; width: 78px; height: 89px;
    border: 2px solid var(--gold); border-radius: 5px;
    background: radial-gradient(circle at 50% 50%, rgba(201,162,74,0.25), rgba(201,162,74,0.05) 60%);
  }
  .basket-illustration {
    position: absolute; left: 380px; top: 332px; width: 48px; height: 50px;
    border-radius: 4px;
    background: linear-gradient(135deg, rgba(201,162,74,0.55), rgba(164,120,42,0.35));
  }

  .feature { position: absolute; top: 291px; display: flex; flex-direction: column; align-items: center; width: 60px; }
  .feature__icon {
    width: 36px; height: 36px; border-radius: 50%;
    border: 1.5px solid var(--gold);
  }
  .feature__label {
    margin-top: 3px; width: 60px; text-align: center;
    font-size: 5px; line-height: 1.2; color: var(--white);
  }
  .feature--clothes { left: 205px; }
  .feature--neutral { left: 267px; }
  .feature-dot { position: absolute; left: 264px; top: 308px; width: 3px; height: 3px; border-radius: 50%; background: var(--gold); }

  .contents-pill {
    position: absolute; left: 193px; top: 355px; width: 147px; height: 18px;
    border: 1.5px solid var(--gold); border-radius: 9px;
    display: flex; align-items: center; overflow: hidden;
    font-size: 11px; line-height: 1;
  }
  .contents-pill__label {
    height: 100%; padding: 0 6px 0 8px; display: flex; align-items: center;
    background: var(--gold); color: var(--box-black); border-radius: 0 9px 9px 0;
  }
  .contents-pill__count { padding-left: 6px; color: var(--gold); }
  .contents-usage {
    position: absolute; left: 200px; top: 373px; width: 128px; height: 8px;
    background: var(--white); border-radius: 0 0 4px 4px;
    font-size: 5px; font-weight: 600; line-height: 8px; letter-spacing: 0.2px;
    text-align: center; color: var(--box-black); white-space: nowrap;
  }
</style>
</head>
<body>
<main class="canvas">
  <section class="box-front" aria-label="Voorzijde verpakking Kribbelnest Wasstrips">
    <div class="box-front__content">
      <div class="halftone-area" role="img" aria-label="Decoratief stippenpatroon in donkergrijs"></div>

      <svg class="window-outline" width="720" height="435" viewBox="0 0 720 435" aria-hidden="true">
        <path d="M628 435 V67 Q628 59 620 59 H101 Q93 59 93 67 V435" fill="none" stroke="var(--line-grey)" stroke-width="1"/>
        <path d="M612 100 V435 M108 100 V435" fill="none" stroke="var(--line-grey)" stroke-width="1.5" stroke-dasharray="6 5"/>
        <path d="M605 100 H619 M101 100 H115" stroke="var(--line-grey)" stroke-width="1"/>
      </svg>

      <p class="brand-name">KRIBBELNEST</p>

      <div class="product-title">
        <h1 class="product-name">WASSTRIPS</h1>
        <svg class="product-badge" viewBox="0 0 78 78" aria-label="Icoon wasstrips">
          <circle cx="39" cy="39" r="39" fill="var(--white)"/>
          <rect x="22" y="18" width="26" height="38" rx="2" fill="none" stroke="var(--box-black)" stroke-width="4" transform="rotate(-12 35 37)"/>
          <rect x="30" y="22" width="26" height="38" rx="2" fill="var(--box-black)" transform="rotate(8 43 41)"/>
        </svg>
      </div>

      <div class="washer-illustration" role="img" aria-label="Illustratie wasmachine in goudlijn"></div>
      <div class="basket-illustration" role="img" aria-label="Illustratie wasmand met kleding"></div>

      <div class="feature feature--clothes">
        <div class="feature__icon" role="img" aria-label="Icoon kleding"></div>
        <p class="feature__label">Voor alle<br>kledingtypes</p>
      </div>
      <span class="feature-dot"></span>
      <div class="feature feature--neutral">
        <div class="feature__icon" role="img" aria-label="Icoon geen geur"></div>
        <p class="feature__label">Neutrale<br>(Geen Geur)</p>
      </div>

      <div class="contents-pill">
        <span class="contents-pill__label">Bevat</span>
        <span class="contents-pill__count">30 wasstrips</span>
      </div>
      <p class="contents-usage">30 WASSTRIPS = 60 WASBEURTEN</p>
    </div>
  </section>

  <aside class="box-side" aria-label="Zijkant verpakking">
    <p class="box-side__brand">KRIBBELNEST</p>
  </aside>
</main>
</body>
</html>
```